Flyer-Design für Vertrieb von LED-Beleuchtung
Zielgruppe
Vertrieb von Led Beleuchtung,, für Biergärten
Shop-Adresse lautet www.brilo-nox-markt.de diese sollte auch unbedingt mit rein!
Aufgabenstellung
Es geht Hauptsächlich nur um Bunte Led Birnen und die dazugehörigen Fassungen.
Daher bitte eigene Bilder benutzen und zusätzlich noch welche suchen die passen würden.
Aussagen soll es wie sehr man durch die Umstellung auf unsere Birnen sparen kann und dass sie besser Leuchten als normale und nicht kaputt gehen. 2 alte Flyerversuche von mir selbst liegen bei zwecks preise etc. Die Antwortkarte darf nicht mehr drauf sein da dies bereits Formatprobleme mit der Post gab

```html
<!DOCTYPE html>
<html lang="de">
<head>
<meta charset="utf-8">
<title>GLIMTEC – Flyer LED-Beleuchtung für Biergärten</title>
<link rel="stylesheet" href="https://fonts.googleapis.com/css2?family=Bebas+Neue&family=Oswald:wght@300;400;500;600&display=swap">
<style>
  :root{
    --stage:#313131;
    --white:#ffffff;
    --black:#000000;
    --magenta:#c2007a;
    --magenta-dark:#6e0f45;
    --blue:#3e60a8;
    --blue-text:#3e60a8;
    --grey-text:#8c8c8c;
    --grey-dark:#6b6b6b;
    --pink-text:#b0006a;
    --pink-bright:#d6118a;
    --c-blau:#4a6bbf;
    --c-gruen:#5aa44a;
    --c-gelb:#f2d21b;
    --c-pink:#d01a8c;
    --ink:#111111;
  }
  *{margin:0;padding:0;box-sizing:border-box}
  html,body{width:915px;height:1200px;overflow:hidden;background:var(--stage)}
  .canvas{position:relative;width:915px;height:1200px;font-family:"Oswald",sans-serif;text-transform:uppercase}
  .sheet{position:absolute;display:flex}
  .sheet--outside{left:107px;top:81px;width:673px;height:476px}
  .sheet--inside{left:103px;top:633px;width:673px;height:476px}
  .panel{position:relative;height:100%;overflow:hidden}
  .brand{font-family:"Bebas Neue",sans-serif;letter-spacing:2px;line-height:1;position:absolute}

  /* outside sheet */
  .panel--bulbs{width:226px;background:var(--white)}
  .bulbs-art{position:absolute;left:55px;top:40px;width:135px;height:400px;
    background:linear-gradient(180deg,#6bbf6b 0%,#e8e8e8 25%,#c85a9a 48%,#f0ea3c 68%,#4f6fc2 88%,#f2f2f2 100%);
    border-radius:60px;opacity:.85}
  .panel--specs{width:227px;background:var(--black);color:var(--white)}
  .panel--specs .brand{left:26px;top:48px;font-size:22px}
  .product-title{position:absolute;left:28px;top:78px;font-family:"Bebas Neue",sans-serif;font-weight:400;font-size:19px;line-height:23px;letter-spacing:.6px}
  .colour-list{position:absolute;left:28px;top:122px;font-family:"Bebas Neue",sans-serif;font-size:14px;letter-spacing:.5px}
  .colour-list .blau{color:var(--c-blau)} .colour-list .gruen{color:var(--c-gruen)}
  .colour-list .gelb{color:var(--c-gelb)} .colour-list .pink{color:var(--c-pink)}
  .tech{position:absolute;left:28px;top:154px;font-size:8.5px;font-weight:500;line-height:12.5px}
  .tech h3{font-size:8.5px;font-weight:500;margin-bottom:5px}
  .tech ul{list-style:none}
  .features{position:absolute;left:0;width:227px;text-align:center;color:var(--grey-text);font-size:10.5px;line-height:17.5px;font-weight:400}
  .features--guarantee{top:266px}
  .features--effects{top:301px}
  .features--eco{top:353px}
  .features--robust{top:424px}
  .panel--sale{width:220px;background:var(--magenta);text-align:center}
  .slogan{position:absolute;top:88px;width:100%;font-family:"Bebas Neue",sans-serif;font-size:24px;line-height:30px;letter-spacing:1px;color:var(--black)}
  .sale-title{position:absolute;top:192px;width:100%;font-family:"Bebas Neue",sans-serif;font-weight:400;font-size:32px;line-height:29px;letter-spacing:1px;color:var(--white)}
  .rule{position:absolute;left:21px;width:181px;height:1px;background:rgba(255,255,255,.7)}
  .rule--top{top:263px}
  .rule--bottom{top:372px}
  .price{position:absolute;top:275px;width:100%;font-family:"Bebas Neue",sans-serif;font-size:29px;color:var(--black)}
  .instead{position:absolute;top:310px;width:100%;font-family:"Bebas Neue",sans-serif;font-size:21px;line-height:24px;color:var(--magenta-dark)}
  .instead s{text-decoration-thickness:1.5px}

  /* inside sheet */
  .panel--claim{width:220px;background:var(--blue)}
  .panel--claim .brand{left:23px;top:86px;font-size:21px;color:var(--black)}
  .claim-small{position:absolute;left:23px;top:115px;font-size:11.5px;line-height:17.3px;font-weight:500;color:var(--ink);letter-spacing:.3px}
  .claim-big{position:absolute;left:23px;top:254px;font-family:"Bebas Neue",sans-serif;font-size:26px;line-height:31px;letter-spacing:1px;color:var(--white)}
  .panel--contact{width:226px;background:var(--black);text-align:center}
  .advice{position:absolute;top:85px;width:100%;font-size:10.5px;line-height:18.2px;font-weight:300;color:var(--pink-text)}
  .advice strong{font-weight:600;color:var(--pink-bright)}
  .panel--contact .brand{left:0;width:100%;top:324px;font-size:22px;color:var(--white)}
  .address{position:absolute;top:362px;width:100%;font-size:10.5px;line-height:14.5px;font-weight:500;color:var(--white);font-style:normal}
  .address .mail{display:block;margin-top:14px}
  .panel--cover{width:227px;background:var(--white)}
  .cover-photo{position:absolute;left:0;top:0;width:227px;height:350px;
    background:radial-gradient(circle at 70% 40%,#ff2a55 0,rgba(255,42,85,0) 22%),radial-gradient(circle at 30% 20%,#1d5fae 0,rgba(29,95,174,0) 30%),linear-gradient(160deg,#0c1a3a 0%,#091230 50%,#04081a 100%)}
  .panel--cover .brand{left:23px;top:372px;font-size:21px;color:var(--black)}
  .cover-line{position:absolute;left:23px;font-family:"Bebas Neue",sans-serif;font-size:13.5px;letter-spacing:.6px}
  .cover-line--blue{top:400px;color:var(--blue-text)}
  .cover-line--grey{top:417px;color:var(--grey-dark)}
</style>
</head>
<body>
<main class="canvas">

  <section class="sheet sheet--outside">
    <div class="panel panel--bulbs">
      <div class="bulbs-art" role="img" aria-label="Fünf bunte LED-Kugelbirnen in Grün, Weiß, Pink, Gelb und Blau mit E27-Sockel, übereinander gestapelt"></div>
    </div>

    <div class="panel panel--specs">
      <div class="brand">GLIMTEC</div>
      <h2 class="product-title">LED-Birne 1 Watt<br>in den Farben:</h2>
      <p class="colour-list"><span class="blau">Blau</span>, <span class="gruen">Grün</span>, Weiss, <span class="gelb">Gelb</span>, <span class="pink">Pink</span></p>
      <div class="tech">
        <h3>Technische Daten</h3>
        <ul>
          <li>Fassung E27</li>
          <li>IP65 spritzwassergeschutzt</li>
          <li>7 Lumen bei 6500K</li>
          <li>Verbrauch 1Watt</li>
          <li>Lebensdauer min. 30.000 Stunden</li>
        </ul>
      </div>
      <p class="features features--guarantee">1 Jahr Garantie auf alle Leuchtmittel</p>
      <p class="features features--effects">Moderne Spezial-Effejkte<br>für Standard-Fassungen</p>
      <p class="features features--eco">Umweltschonend durch niedrigen<br>Stromverbrauch von nur 1 Watt und<br>von sehr langer Lebensdauer</p>
      <p class="features features--robust">Robustes und stossfestes Material</p>
    </div>

    <div class="panel panel--sale">
      <p class="slogan">Damit Sie nicht<br>im Dunklen sitzen</p>
      <h2 class="sale-title">Sommer-Sale<br>Preis</h2>
      <div class="rule rule--top"></div>
      <p class="price">2,27 Euro</p>
      <p class="instead">statt<br><s>2,78 Euro</s></p>
      <div class="rule rule--bottom"></div>
    </div>
  </section>

  <section class="sheet sheet--inside">
    <div class="panel panel--claim">
      <div class="brand">GLIMTEC</div>
      <p class="claim-small">Sparen Sie nicht an Personal<br>oder Qualität, sondern<br>an kostenspieliger<br>Aussenbeleuchtung</p>
      <p class="claim-big">Viel bewegen<br>durch einfaches<br>Austauschen und<br>umsteigen auf<br>umweltschonende<br>LED-Birnen</p>
    </div>

    <div class="panel panel--contact">
      <p class="advice">Gerne beraten wir Sie über<br><strong>individuelle Möglichkeiten,</strong><br>Ihren Biergarten<br>perfekt auszuleuchten und<br>neue Akzente zu setzen.</p>
      <div class="brand">GLIMTEC</div>
      <address class="address">Jelu Pandor<br>Wiesenrainstr. 7<br>71234 Talbrunn am Hang<span class="mail">Mail: info@glimtec-licht.de</span></address>
    </div>

    <div class="panel panel--cover">
      <div class="cover-photo" role="img" aria-label="Nachtaufnahme eines Gerüsts mit vielen bunten, unscharfen Lichterpunkten in Blau und Rot"></div>
      <div class="brand">GLIMTEC</div>
      <p class="cover-line cover-line--blue">Stromsparende LED-Beleuchtung</p>
      <p class="cover-line cover-line--grey">für Ihren Biergarten</p>
    </div>
  </section>

</main>
</body>
</html>
```